Law Office Business Card

We need a business card design to include the following information:
Name of Firm: Brennick Law Group, P.A.
Address: 4627 Sandlot Ave, Ste 208, West Palm Beach, FL 33409
Phone: 561-555-0148
Fax: 561-555-0193
Website: http://www.tbrennicklaw.example

We Need a place for the Person's name and email address. Please start with the following:
Lorna K. Dwyer, Esq.
lorna@tbrennicklaw.example

```html
<!DOCTYPE html>
<html lang="en">
<head>
<meta charset="utf-8">
<title>Brennick Law Group – Business Card</title>
<link href="https://fonts.googleapis.com/css2?family=Cormorant+Garamond:wght@500&family=Open+Sans:wght@400;700&display=swap" rel="stylesheet">
<style>
  :root {
    --page-bg: #e9e7e3;
    --card-white: #f6f9fb;
    --brand-grey: #7f7a74;
    --panel-top: #2479a4;
    --panel-bottom: #175a80;
    --panel-strip: rgba(255, 255, 255, 0.07);
    --panel-divider: rgba(255, 255, 255, 0.12);
    --name-white: #ffffff;
    --detail-blue: #78c6ec;
    --email-white: #e8f2f8;
  }
  html, body {
    margin: 0;
    padding: 0;
    width: 1200px;
    height: 993px;
    overflow: hidden;
    background: var(--page-bg);
  }
  .business-card {
    position: absolute;
    left: 100px;
    top: 211px;
    width: 1000px;
    height: 571px;
    display: flex;
    background: var(--card-white);
    box-shadow: 0 8px 24px rgba(0,0,0,0.12);
    overflow: hidden;
  }
  .brand-side {
    width: 440px;
    position: relative;
    background: var(--card-white);
  }
  .brand-mark {
    position: absolute;
    left: 90px;
    top: 150px;
    display: flex;
    align-items: center;
    gap: 16px;
  }
  .brand-square {
    width: 40px;
    height: 40px;
    border: 2px solid var(--brand-grey);
    box-sizing: border-box;
  }
  .brand-name {
    font-family: "Cormorant Garamond", serif;
    font-weight: 500;
    font-size: 34px;
    line-height: 1.05;
    color: var(--brand-grey);
  }
  .firm-name {
    position: absolute;
    left: 44px;
    top: 340px;
    font-family: "Cormorant Garamond", serif;
    font-weight: 500;
    font-size: 39px;
    color: var(--brand-grey);
    white-space: nowrap;
  }
  .contact-side {
    flex: 1;
    position: relative;
    background: linear-gradient(180deg, var(--panel-top) 0%, var(--panel-top) 30%, var(--panel-bottom) 100%);
    font-family: "Open Sans", sans-serif;
  }
  .attorney-name {
    position: absolute;
    right: 46px;
    top: 82px;
    margin: 0;
    font-weight: 700;
    font-size: 32px;
    letter-spacing: 2.5px;
    color: var(--name-white);
  }
  .email-strip {
    position: absolute;
    left: 0;
    right: 0;
    top: 170px;
    height: 60px;
    background: var(--panel-strip);
    border-top: 1px solid var(--panel-divider);
    border-bottom: 1px solid var(--panel-divider);
    display: flex;
    align-items: center;
    padding-left: 46px;
    gap: 14px;
    font-size: 23px;
    letter-spacing: 1px;
    color: var(--email-white);
  }
  .contact-list {
    position: absolute;
    left: 46px;
    top: 262px;
    margin: 0;
    padding: 0;
    list-style: none;
    color: var(--detail-blue);
    font-size: 23px;
    letter-spacing: 1px;
    line-height: 1.3;
  }
  .contact-list li {
    display: flex;
    align-items: flex-start;
    gap: 14px;
  }
  .contact-list .address { margin-bottom: 16px; }
  .icon {
    flex: none;
    width: 22px;
    height: 22px;
    margin-top: 4px;
  }
</style>
</head>
<body>
  <div class="business-card">
    <section class="brand-side">
      <div class="brand-mark">
        <span class="brand-square"></span>
        <span class="brand-name">Brennick Law Group</span>
      </div>
      <div class="firm-name">Brennick Law Group, P.A.</div>
    </section>

    <section class="contact-side">
      <h1 class="attorney-name">Lorna K. Dwyer, Esq.</h1>

      <div class="email-strip">
        <svg class="icon" viewBox="0 0 24 24" fill="none" stroke="currentColor" stroke-width="1.8" style="margin-top:0">
          <rect x="2" y="5" width="20" height="14" rx="1"/>
          <path d="M2 6l10 7 10-7"/>
        </svg>
        <span>lorna@tbrennicklaw.example</span>
      </div>

      <ul class="contact-list">
        <li class="address">
          <svg class="icon" viewBox="0 0 24 24" fill="currentColor">
            <path d="M12 2a7 7 0 0 0-7 7c0 5 7 13 7 13s7-8 7-13a7 7 0 0 0-7-7zm0 9.5A2.5 2.5 0 1 1 12 6.5a2.5 2.5 0 0 1 0 5z"/>
          </svg>
          <span>4627 Sandlot Ave, Ste 208,<br>West Palm Beach, FL 33409</span>
        </li>
        <li>
          <svg class="icon" viewBox="0 0 24 24" fill="currentColor">
            <path d="M6.6 10.8a15 15 0 0 0 6.6 6.6l2.2-2.2a1 1 0 0 1 1-.25 11.4 11.4 0 0 0 3.6.57 1 1 0 0 1 1 1V20a1 1 0 0 1-1 1A17 17 0 0 1 3 4a1 1 0 0 1 1-1h3.5a1 1 0 0 1 1 1c0 1.25.2 2.45.57 3.6a1 1 0 0 1-.25 1z"/>
          </svg>
          <span>561-555-0148</span>
        </li>
        <li>
          <svg class="icon" viewBox="0 0 24 24" fill="currentColor">
            <path d="M7 3h10v5H7zM4 9h16a1 1 0 0 1 1 1v7h-4v4H7v-4H3v-7a1 1 0 0 1 1-1zm5 7v3h6v-3z"/>
          </svg>
          <span>561-555-0193</span>
        </li>
        <li>
          <svg class="icon" viewBox="0 0 24 24" fill="none" stroke="currentColor" stroke-width="1.8">
            <circle cx="12" cy="12" r="9"/>
            <path d="M3 12h18M12 3c3 3 3 15 0 18M12 3c-3 3-3 15 0 18"/>
          </svg>
          <span>www.tbrennicklaw.example</span>
        </li>
      </ul>
    </section>
  </div>
</body>
</html>
```